RTV Engineering Business Card Design

We’re looking for an elegant, clean, and timeless business card design that communicates experience, capability, and reliability.

RTV Engineering was established in 1995 , we are a Government Contracting company providing Professional Services to the Department of Harbor Affairs, Frontier Resilience and the Signals Consortium. Our capabilities include: Acquisition & Program Management; Intelligence & Security Operations; Cyber, IT & Network Operations; Lifecycle Logistics & Asset Readiness; C5ISR Systems Engineering & Sustainment.

We want the card to reflect a straightforward, confident approach to business. The design should feel polished and professional without being flashy or overly corporate.

Design Direction
Clean, sophisticated, and uncluttered
Elegant but understated
Strong typography and thoughtful spacing
A timeless aesthetic rather than something overly trendy
Confident and established, with a sense of substance
Easy to read and practical in a real-world business setting

The overall impression should be: “These are experienced professionals who know what they’re doing, do what they say, and can be relied upon.”

We’re open to creative interpretations. The finished card should feel distinctive through its typography, proportions, layout, and attention to detail rather than through excessive graphics or visual effects.

We’re looking for a design that would make a potential client immediately feel that they’re dealing with a capable, trustworthy, and established company.

Company Colors: Navy and Gold/Yellow (but you do not need to use these colors on the card)
Company Name: RTV Engineering Associates, Inc. (known as RTV Engineering)
Website: rtvengineering-hq.example
Company Logo: Navy & Gold (other variations attached)

```html
<!DOCTYPE html>
<html lang="en">
<head>
<meta charset="utf-8">
<title>RTV Engineering – Business Card</title>
<link rel="stylesheet" href="https://fonts.googleapis.com/css2?family=Montserrat:wght@400;500;700&display=swap">
<style>
  :root {
    --page-bg: #e2ddd6;
    --card-bg: #f4f1ec;
    --card-edge: #dcd6cd;
    --gold: #c9a227;
    --gold-light: #ddb93b;
    --ink: #2a2a2a;
    --band: #111111;
  }
  * { margin: 0; padding: 0; box-sizing: border-box; }
  html, body {
    width: 1200px;
    height: 1047px;
    overflow: hidden;
    background: var(--page-bg);
    font-family: "Montserrat", Arial, sans-serif;
  }
  .card {
    position: absolute;
    left: 100px;
    top: 251px;
    width: 1000px;
    height: 545px;
    background: var(--card-bg);
    border: 1px solid var(--card-edge);
    border-radius: 24px;
    overflow: hidden;
  }
  .brand-name {
    position: absolute;
    left: 118px;
    top: 270px;
    font-size: 34px;
    font-weight: 700;
    color: var(--ink);
    letter-spacing: -0.3px;
    white-space: nowrap;
  }
  .divider {
    position: absolute;
    left: 500px;
    top: 125px;
    width: 2px;
    height: 295px;
    background: var(--gold);
  }
  .details {
    position: absolute;
    left: 541px;
    top: 118px;
    color: var(--ink);
  }
  .person-name {
    font-size: 38px;
    font-weight: 700;
    color: var(--gold);
    letter-spacing: 0.5px;
    line-height: 1.1;
  }
  .person-title {
    font-size: 24px;
    font-weight: 400;
    margin-top: 8px;
  }
  .address {
    font-size: 23px;
    line-height: 38px;
    margin-top: 18px;
    letter-spacing: 0.3px;
  }
  .contact-list {
    list-style: none;
    margin-top: 18px;
    font-size: 23px;
    line-height: 38px;
    letter-spacing: 0.3px;
  }
  .contact-list li {
    display: flex;
    align-items: center;
    gap: 12px;
  }
  .contact-icon {
    width: 18px;
    height: 18px;
    flex: none;
  }
  .card-wave {
    position: absolute;
    left: 0;
    bottom: 0;
    width: 1000px;
    height: 545px;
  }
</style>
</head>
<body>
  <section class="card">
    <svg class="card-wave" viewBox="0 0 1000 545" aria-hidden="true">
      <path d="M0 466 Q 160 488 330 504 Q 170 498 0 486 Z" fill="var(--gold)"/>
      <path d="M610 497 Q 800 478 1000 476 L1000 490 Q 800 492 610 499 Z" fill="var(--gold-light)"/>
      <path d="M0 486 Q 300 522 600 503 Q 820 490 1000 490 L1000 545 L0 545 Z" fill="var(--band)"/>
    </svg>

    <div class="brand-name">RTV Engineering</div>

    <div class="divider"></div>

    <div class="details">
      <h1 class="person-name">MARA QUELLEN</h1>
      <p class="person-title">Managing Director</p>
      <p class="address">4820 Harlow Avenue, Suite<br>310, Portsmouth Bay, VA 23999</p>
      <ul class="contact-list">
        <li>
          <svg class="contact-icon" viewBox="0 0 20 20" aria-hidden="true">
            <path d="M3 7 Q10 1 17 7 L15 10 L12 8 L8 8 L5 10 Z" fill="var(--gold)"/>
            <rect x="5" y="10" width="10" height="7" rx="1.5" fill="var(--gold)"/>
          </svg>
          555-014-2290
        </li>
        <li>
          <svg class="contact-icon" viewBox="0 0 20 20" aria-hidden="true">
            <rect x="2" y="5" width="16" height="11" rx="1" fill="var(--gold)"/>
            <path d="M2.5 5.5 L10 11 L17.5 5.5" fill="none" stroke="var(--card-bg)" stroke-width="1.4"/>
          </svg>
          info@rtvengineering-hq.example
        </li>
        <li>
          <svg class="contact-icon" viewBox="0 0 20 20" aria-hidden="true">
            <circle cx="10" cy="10" r="8" fill="var(--gold)"/>
            <path d="M6 6 Q9 8 8 11 Q6 12 6 14 M12 4 Q11 8 14 9 Q15 12 13 15" fill="none" stroke="var(--card-bg)" stroke-width="1.3"/>
          </svg>
          rtvengineering-hq.example
        </li>
      </ul>
    </div>
  </section>
</body>
</html>
```